Business Card Design Project

I require a business card with the following information on them for various different people;
name
m:
f:
e:
I have a logo already and will attached that. We are in the construction industry. I require something clean and simple but eye catching at the same time. You can use another colour with our logo if you like and you can style the logo as well if you wish. I am open.
Also it needs to be front and back design.
Industry/Entity Type
Construction
Requirements
Must have
- Logo, name, mobile, fax and email address.
Front and back design

```html
<!DOCTYPE html>
<html lang="en">
<head>
<meta charset="utf-8">
<title>Northgate Ridge Builders – Business Cards</title>
<link href="https://fonts.googleapis.com/css2?family=Questrial&display=swap" rel="stylesheet">
<style>
  :root {
    --page-bg: #ffffff;
    --burgundy-light: #7a0042;
    --burgundy: #5e0033;
    --burgundy-dark: #3f0022;
    --brand-green: #7ac943;
    --accent-green: #8fd14f;
    --silver-edge: #4a4a4a;
    --silver-mid: #bcbcbc;
    --silver-bright: #f4f4f4;
    --ink: #1a1a1a;
    --label: #6a0a38;
    --white: #ffffff;
  }
  * { margin: 0; padding: 0; box-sizing: border-box; }
  html, body {
    width: 1200px; height: 900px; overflow: hidden;
    background: var(--page-bg);
    font-family: "Questrial", "Century Gothic", sans-serif;
  }
  .canvas { position: relative; width: 1200px; height: 900px; }

  .card {
    position: absolute;
    width: 720px; height: 410px;
    border-radius: 30px;
    overflow: hidden;
    background: radial-gradient(ellipse at 30% 0%, var(--burgundy-light) 0%, var(--burgundy) 45%, var(--burgundy-dark) 100%);
    box-shadow: 0 6px 18px rgba(0,0,0,0.18);
  }
  .card--front { left: 160px; top: 30px; }
  .card--back  { left: 320px; top: 465px; }

  .brand {
    position: absolute; left: 0; right: 0;
    display: flex; align-items: center; justify-content: center; gap: 14px;
  }
  .brand__mark {
    width: 30px; height: 30px; background: var(--brand-green);
  }
  .brand__name {
    color: var(--brand-green);
    font-size: 40px; font-weight: 400; letter-spacing: 1px;
  }
  .card--front .brand { top: 80px; }
  .card--back .brand  { top: 130px; }

  .silver-band {
    position: absolute; left: 0; right: 0;
    background: linear-gradient(90deg, var(--silver-edge) 0%, var(--silver-mid) 22%, var(--silver-bright) 55%, var(--silver-mid) 80%, var(--silver-edge) 100%);
  }
  .hairline {
    position: absolute; left: 0; right: 0; height: 3px;
    background: linear-gradient(90deg, var(--silver-edge), var(--silver-bright) 55%, var(--silver-edge));
  }

  .card--front .hairline { top: 222px; }
  .card--front .silver-band { top: 282px; height: 98px; }
  .holder-name {
    position: absolute; left: 40px; top: 236px;
    color: var(--white); font-size: 32px; letter-spacing: 1.5px;
  }
  .contact {
    position: absolute; left: 0; right: 0; top: 296px;
    text-align: center; font-size: 21px; line-height: 34px; color: var(--ink);
  }
  .contact__label { color: var(--label); }
  .contact__gap { display: inline-block; width: 22px; }

  .card--back .accent-line {
    position: absolute; left: 0; right: 0; top: 300px; height: 3px;
    background: var(--accent-green);
  }
  .card--back .silver-band { top: 303px; height: 70px; }
</style>
</head>
<body>
<main class="canvas">

  <section class="card card--front" aria-label="Business card front">
    <div class="brand">
      <span class="brand__mark"></span>
      <span class="brand__name">Northgate Ridge Builders</span>
    </div>
    <div class="hairline"></div>
    <h1 class="holder-name">YOUR NAME</h1>
    <div class="silver-band"></div>
    <div class="contact">
      <p><span class="contact__label">Mobile :</span> xxxxxxxxxx<span class="contact__gap"></span><span class="contact__label">Fax :</span> xxx-xxx-xxxx</p>
      <p><span class="contact__label">E-mail :</span> name@website.com</p>
    </div>
  </section>

  <section class="card card--back" aria-label="Business card back">
    <div class="brand">
      <span class="brand__mark"></span>
      <span class="brand__name">Northgate Ridge Builders</span>
    </div>
    <div class="accent-line"></div>
    <div class="silver-band"></div>
  </section>

</main>
</body>
</html>
```